Web page design for a startup, no coding

Quillbrook is a Data mining startup helping companies get data from websites. We’re looking to revamp our website to make it more professional and conversation friendly.
I need a designer to design the website in PSD and Once the PSD is done, the HTML design will be awarded as a separate job. We’ll need continues improvements to the design based on the user behaviour in the site and this can be a long term work for the right designer.
Read the details on the attached document
Target Market(s)
Big data, Data Mining
Industry/Entity Type
Business Software
Number of Pages Required
5+ page
Requirements
Must have
- Refer to the doc
Nice to have
- Refer to the doc
Should not have
- Refer to the doc

```html
<!DOCTYPE html>
<html lang="en">
<head>
<meta charset="utf-8">
<title>Quillbrook — Structured Data Feeds</title>
<link rel="stylesheet" href="https://fonts.googleapis.com/css2?family=Mulish:wght@400;500;600;700&display=swap">
<style>
:root{
  --amber:#ffa800;
  --amber-deep:#f7a200;
  --amber-light:#ffc233;
  --ink:#1b1b1b;
  --muted:#777;
  --soft:#f2f2f2;
  --hex-grey:#7a7a7a;
  --white:#fff;
  --line:#d9d9d9;
  --desk-a:#eef0f3;
  --desk-b:#dfe3e8;
}
*{box-sizing:border-box;margin:0;padding:0}
html,body{width:1200px;height:2456px;overflow:hidden}
body{font-family:"Mulish",sans-serif;color:var(--ink);background:var(--white);position:relative}
.abs{position:absolute}

/* hero */
.hero{position:absolute;left:0;top:0;width:1200px;height:585px;background:linear-gradient(135deg,var(--amber-light),var(--amber) 50%,var(--amber-deep))}
.hero-art{position:absolute;inset:0;background:radial-gradient(ellipse at 35% 70%,rgba(255,220,90,.45),transparent 55%),radial-gradient(ellipse at 80% 60%,rgba(255,210,60,.4),transparent 50%)}
.brand{position:absolute;left:159px;top:36px;display:flex;align-items:center;gap:12px;color:var(--white);font-weight:500;font-size:36px;letter-spacing:.5px}
.brand-mark{width:26px;height:26px;border:3px solid currentColor;border-radius:3px}
.nav{position:absolute;top:46px;right:173px;display:flex;gap:28px}
.nav a{color:var(--white);text-decoration:none;font-size:18px;font-weight:600}
.hero-title{position:absolute;top:222px;left:0;width:1200px;text-align:center;color:var(--white);font-size:36px;font-weight:600}
.hero-sub{position:absolute;top:280px;left:170px;width:860px;text-align:center;color:var(--white);font-size:19px;line-height:27px}
.btn-dark{position:absolute;left:519px;top:355px;width:169px;height:40px;background:#000;color:var(--white);font-size:17px;font-weight:600;display:flex;align-items:center;justify-content:center}
.dots{position:absolute;top:558px;left:560px;display:flex;gap:9px}
.dots span{width:13px;height:13px;border-radius:50%;background:var(--white)}
.dots span:first-child{background:transparent;border:2px solid var(--white)}

/* clients */
.clients{position:absolute;top:585px;left:0;width:1200px;height:107px;display:flex;justify-content:center;align-items:center;gap:52px}
.client{font-size:26px;font-weight:600;color:#555}
.client.first{color:#d0321e}

/* uses */
.uses{position:absolute;top:692px;left:0;width:1200px;height:528px;background:var(--soft)}
.uses-title{position:absolute;top:60px;left:0;width:1200px;text-align:center;font-size:25px;line-height:35px;font-weight:500}
.use{position:absolute;width:420px}
.use h3{font-size:17px;font-weight:500;margin-bottom:6px}
.use p{font-size:11.5px;line-height:17px;color:var(--muted)}
.use.left{text-align:right;left:43px}
.use.right{left:725px}
.use-icon{position:absolute;width:72px;height:72px;border-radius:50%;background:var(--white);border:2px solid #ddd;display:flex;align-items:center;justify-content:center}

/* why */
.why-title{position:absolute;top:1276px;left:0;width:1200px;text-align:center;font-size:29px;font-weight:500}
.hex{position:absolute;top:1319px;width:224px;height:256px}
.hex svg{position:absolute;inset:0}
.hex-body{position:absolute;left:22px;right:22px;top:58px;text-align:center;color:var(--white)}
.hex-body .ico{height:54px;display:flex;justify-content:center}
.hex-body h3{font-size:16px;font-weight:700;margin:12px 0 6px}
.hex-body p{font-size:10.5px;line-height:16px;opacity:.9}

/* contact */
.contact{position:absolute;top:1637px;left:0;width:1200px;height:478px;background:linear-gradient(120deg,var(--desk-a),#f6f7f9 50%,var(--desk-b))}
.contact h2{position:absolute;top:48px;width:1200px;text-align:center;font-size:29px;font-weight:500}
.contact .lead{position:absolute;top:100px;width:1200px;text-align:center;font-size:18px;line-height:28px;color:#444}
.field{position:absolute;background:var(--white);border:1px solid #bbb;font-size:13px;color:#555;padding:11px 18px}
.btn-amber{position:absolute;left:535px;top:391px;width:135px;height:36px;background:var(--amber);color:var(--white);font-weight:700;font-size:14px;display:flex;align-items:center;justify-content:center}

/* footer */
.foot-head{position:absolute;top:2166px;font-size:20px;color:var(--amber);font-weight:500}
.foot-list{position:absolute;top:2202px;list-style:none;font-size:14px;color:#555;line-height:28px}
.social{position:absolute;top:2202px;left:618px;display:flex;gap:11px}
.social span{width:32px;height:32px;border-radius:50%;background:var(--amber)}
.foot-brand{position:absolute;left:840px;top:2186px;display:flex;align-items:center;gap:12px;color:#888;font-size:36px;font-weight:500}
.foot-brand .brand-mark{border-color:#888}
.rule{position:absolute;left:157px;top:2390px;width:886px;height:1px;background:var(--line)}
.copy{position:absolute;top:2405px;width:1200px;text-align:center;font-size:11.5px;color:#999}
</style>
</head>
<body>

<header class="hero">
  <div class="hero-art" role="img" aria-label="Photo of stacked data sheets tinted amber"></div>
  <div class="brand"><span class="brand-mark"></span>Quillbrook</div>
  <nav class="nav"><a>Solutions</a><a>Pricing</a><a>Company</a><a>Get free Quote</a></nav>
  <h1 class="hero-title">Turn Websites Into Structured Data feeds</h1>
  <p class="hero-sub">Easily get structured data feeds from any website through our cloud based data&nbsp; as a service platform. No programming ,Servers or Expensive Softwares required</p>
  <div class="btn-dark">Get free Quote</div>
  <div class="dots"><span></span><span></span><span></span><span></span></div>
</header>

<section class="clients">
  <span class="client first">Brixel</span>
  <span class="client">Tallyway</span>
  <span class="client">Corvana</span>
  <span class="client">Merrow</span>
  <span class="client">Launchkin</span>
  <span class="client">Hartwell</span>
</section>

<section class="uses">
  <h2 class="uses-title">Businesses of all sizes use our clean data feeds to Quickly build apps,<br>Experiment with fresh ideas and Solve business problems</h2>

  <div class="use left" style="top:195px"><h3>ECommerce</h3><p>Our Ecommerce product data feeds gives you access<br>to structured product information like pricing,,</p></div>
  <div class="use-icon" style="left:478px;top:187px"><svg width="38" height="34" viewBox="0 0 38 34" fill="none" stroke="#ffa800" stroke-width="2"><rect x="2" y="2" width="34" height="28" rx="2"/><path d="M2 8h34M10 14h3l3 9h10l2-6H15"/><circle cx="17" cy="26" r="1.5"/><circle cx="25" cy="26" r="1.5"/></svg></div>

  <div class="use left" style="top:290px"><h3>Lead Generation</h3><p>We help find quality leads for your business by<br>extracting public&nbsp; data from all kind of sources like</p></div>
  <div class="use-icon" style="left:478px;top:283px"><svg width="38" height="36" viewBox="0 0 38 36" fill="#ffa800"><circle cx="19" cy="9" r="6"/><circle cx="8" cy="13" r="4.5"/><circle cx="30" cy="13" r="4.5"/><path d="M9 34c0-9 4-16 10-16s10 7 10 16z"/><path d="M1 30c0-7 3-11 7-11 2 0 3 1 4 2-2 3-3 6-3 9zM37 30c0-7-3-11-7-11-2 0-3 1-4 2 2 3 3 6 3 9z"/></svg></div>

  <div class="use left" style="top:395px"><h3>SERP Tracking</h3><p>Our SERP data feeds gives companies access to<br>Search Engine rankings of any keywords from search</p></div>
  <div class="use-icon" style="left:478px;top:387px"><svg width="40" height="30" viewBox="0 0 40 30" fill="none" stroke="#ffa800" stroke-width="2"><path d="M2 20l7-6 6 5 4-4"/><circle cx="25" cy="13" r="6"/><path d="M29 17l6 6M30 8l8-6"/></svg></div>

  <div class="use-icon" style="left:635px;top:187px"><svg width="34" height="34" viewBox="0 0 34 34" fill="none" stroke="#ffa800" stroke-width="2"><rect x="6" y="3" width="25" height="28"/><path d="M2 10v21h4M11 10h15M11 15h15M11 20h15M11 25h10"/></svg></div>
  <div class="use right" style="top:195px"><h3>News Aggregation</h3><p>We help businesses&nbsp; build their own unique news<br>data feeds by aggregating data from news sites</p></div>

  <div class="use-icon" style="left:635px;top:283px"><svg width="38" height="38" viewBox="0 0 38 38" fill="none" stroke="#ffa800" stroke-width="2"><circle cx="19" cy="19" r="13"/><circle cx="19" cy="19" r="6" fill="#ffa800"/><path d="M19 1v9M19 28v9M1 19h9M28 19h9"/></svg></div>
  <div class="use right" style="top:290px"><h3>Recruiting</h3><p>We&nbsp; help recruiters&nbsp; automate scouting candidate<br>profiles from different online sources</p></div>

  <div class="use-icon" style="left:635px;top:387px"><svg width="24" height="38" viewBox="0 0 24 38" fill="none" stroke="#ffa800" stroke-width="2"><rect x="2" y="2" width="20" height="34" rx="3"/><path d="M2 8h20M2 29h20"/><circle cx="12" cy="32.5" r="1.3" fill="#ffa800"/></svg></div>
  <div class="use right" style="top:395px"><h3>Build your App</h3><p>We help businesses quickly build their apps on top<br>of our scalable data extraction infrastructure</p></div>
</section>

<h2 class="why-title">Why Us</h2>

<div class="hex" style="left:150px">
  <svg viewBox="0 0 224 256"><polygon points="112,0 224,64 224,192 112,256 0,192 0,64" fill="var(--amber)"/></svg>
  <div class="hex-body">
    <div class="ico"><svg width="52" height="52" viewBox="0 0 52 52" fill="none" stroke="#fff" stroke-width="2"><path d="M4 4h16v6a4 4 0 108 0V4h16v16h-6a4 4 0 100 8h6v16H28v-6a4 4 0 10-8 0v6H4V28h6a4 4 0 100-8H4z"/></svg></div>
    <h3>Solve Real Problems</h3>
    <p>Quillbrook provides a fully managed Big Data As A Service .You can easily plug our data feeds into your favourite</p>
  </div>
</div>

<div class="hex" style="left:374px">
  <svg viewBox="0 0 224 256"><polygon points="112,0 224,64 224,192 112,256 0,192 0,64" fill="var(--hex-grey)"/></svg>
  <div class="hex-body">
    <div class="ico"><svg width="48" height="54" viewBox="0 0 48 54" fill="none" stroke="#fff" stroke-width="2.5"><ellipse cx="24" cy="8" rx="21" ry="6"/><path d="M3 8v38c0 3.3 9.4 6 21 6s21-2.7 21-6V8M3 20c0 3.3 9.4 6 21 6s21-2.7 21-6M3 33c0 3.3 9.4 6 21 6s21-2.7 21-6"/></svg></div>
    <h3>Clean Data</h3>
    <p>We follow a strict quality assurance process and a Machine learning based Q&amp;A system to&nbsp; ensure the</p>
  </div>
</div>

<div class="hex" style="left:598px">
  <svg viewBox="0 0 224 256"><polygon points="112,0 224,64 224,192 112,256 0,192 0,64" fill="var(--amber)"/></svg>
  <div class="hex-body">
    <div class="ico"><svg width="52" height="44" viewBox="0 0 52 44" fill="none" stroke="#fff" stroke-width="2.5"><path d="M3 2v40h47"/><path d="M9 34l12-13 8 7 16-17"/><path d="M36 11h9v9"/></svg></div>
    <h3>Customer Success</h3>
    <p>Ensuring Customer success is our first priority. Our customer success team consists of&nbsp; experienced</p>
  </div>
</div>

<div class="hex" style="left:822px">
  <svg viewBox="0 0 224 256"><polygon points="112,0 224,64 224,192 112,256 0,192 0,64" fill="var(--hex-grey)"/></svg>
  <div class="hex-body">
    <div class="ico"><svg width="62" height="58" viewBox="0 0 62 58" fill="none" stroke="#fff" stroke-width="2"><text x="18" y="9" fill="#fff" stroke="none" font-size="8" font-family="monospace">1010</text><text x="18" y="19" fill="#fff" stroke="none" font-size="8" font-family="monospace">0110</text><text x="18" y="29" fill="#fff" stroke="none" font-size="8" font-family="monospace">1001</text><path d="M2 40h8v16H2zM10 42c6-3 12-3 18 0h8c3 0 3 4 0 4h-10M10 54c8 1 16 0 24-4l20-11c3-2 1-6-2-5l-16 7"/></svg></div>
    <h3>Data Wrangling Support</h3>
    <p>Quillbrook&nbsp; helps those who need data wrangling support by providing profiling, filtering</p>
  </div>
</div>

<section class="contact" role="img" aria-label="Photo of a white desk with keyboard, notebook and coffee cup">
  <h2>We’re here to help!</h2>
  <p class="lead">We're friendly and available to help solve your data extraction problems.<br>Fill the form below to contact us. Let us do the heavy lifting for youa</p>
  <div class="field" style="left:291px;top:192px;width:379px;height:37px">Email address</div>
  <div class="field" style="left:676px;top:192px;width:233px;height:37px">Your Monthly Budget</div>
  <div class="field" style="left:291px;top:241px;width:618px;height:132px">Your Message</div>
  <div class="btn-amber">SUBMIT</div>
</section>

<h4 class="foot-head" style="left:157px">Quick Links</h4>
<ul class="foot-list" style="left:160px"><li>Blog</li><li>Answers</li><li>Case Studies</li><li>Slide</li></ul>
<h4 class="foot-head" style="left:378px">Resources</h4>
<ul class="foot-list" style="left:382px"><li>Startup Partner program</li><li>FAQ</li><li>Careers</li></ul>
<h4 class="foot-head" style="left:617px">Follow Us</h4>
<div class="social" aria-label="Social links"><span></span><span></span><span></span><span></span></div>
<div class="foot-brand"><span class="brand-mark"></span>Quillbrook</div>
<div class="rule"></div>
<p class="copy">© 2016 Company Name&nbsp; All right reserved&nbsp; Term of Use</p>

</body>
</html>
```